Speisekarten-Design für Tennis- und Freizeitanlage mit Restaurant und Biergarten
Zielgruppe
Tennis- und Freizeitanlage mit Restaurant und Biergarten. Zielgruppe von Jung bis Alt
Aufgabenstellung
Speise- und Getränkekarte. Klassisch und klar strukturiert. Möglichst zum selbst ausdrucken (kein Randloses Design) Möglichkeit zum selbstständigen ändern als Word Dokument. A4 Format. Hülle der Speisekarte bereits vorhanden. Siehe Fotos
Wenn möglich farbiges Logo verwenden. Alternativ habe ich noch eine schwarz weiß Variante hinzugefügt.

```html
<!DOCTYPE html>
<html lang="de">
<head>
<meta charset="utf-8">
<title>Speisekarte – Clubhaus Grünau</title>
<link rel="stylesheet" href="https://fonts.googleapis.com/css2?family=Playfair+Display:wght@500&family=Inter:wght@400;500&display=swap">
<style>
  :root {
    --backdrop: #f2f0e6;
    --paper: #f8f8f6;
    --court-green: #5f8f3a;
    --line-green: #4d7a33;
    --ink: #1f2e2f;
    --gold: #c9a03a;
    --ball: #b9d531;
    --net-light: #ece6d8;
    --net-dark: #d8ccb4;
    --text-light: #eef3e6;
  }
  * { box-sizing: border-box; margin: 0; padding: 0; }
  html, body { width: 1200px; height: 900px; overflow: hidden; }
  body { background: var(--backdrop); position: relative; font-family: "Inter", sans-serif; }

  .menu-folder { position: absolute; left: 235px; top: 98px; width: 731px; height: 705px; display: flex; gap: 2px; }

  .back-panel { position: relative; width: 296px; height: 100%; background: var(--paper); overflow: hidden; }
  .back-intro { position: absolute; top: 88px; width: 100%; text-align: center; font-size: 9.5px; letter-spacing: .06em; line-height: 1.35; color: var(--ink); text-transform: uppercase; }
  .net-area { position: absolute; left: 0; top: 214px; width: 100%; height: 136px; background: linear-gradient(180deg, var(--net-light), var(--net-dark)); }
  .net-band { position: absolute; left: 0; top: 200px; width: 100%; height: 40px; }
  .court-section { position: absolute; left: 0; top: 350px; width: 100%; height: 355px; background: var(--court-green); }
  .court-lines { position: absolute; inset: 0; }
  .terrace-photo { position: absolute; left: 35px; top: 21px; width: 228px; height: 123px; border: 2px solid #3f6b28; background: linear-gradient(180deg, #2f5a3a 0%, #4a6e3c 35%, #b5553a 60%, #8a3a28 100%); }
  .season-note { position: absolute; top: 222px; width: 100%; text-align: center; color: var(--text-light); font-size: 9.5px; letter-spacing: .08em; line-height: 1.3; text-transform: uppercase; }
  .season-from { position: absolute; top: 289px; width: 100%; text-align: center; color: var(--text-light); font-size: 9px; font-weight: 500; }
  .back-footer { position: absolute; top: 329px; width: 100%; text-align: center; color: var(--text-light); font-size: 6.5px; letter-spacing: .04em; white-space: nowrap; }

  .cover-panel { position: relative; flex: 1; height: 100%; background: var(--paper); overflow: hidden; }
  .cover-ornament { position: absolute; inset: 0;
    background:
      radial-gradient(circle at 0 0, rgba(201,160,58,.10), transparent 45%),
      radial-gradient(circle at 100% 0, rgba(77,122,51,.10), transparent 45%),
      radial-gradient(circle at 0 100%, rgba(77,122,51,.10), transparent 45%),
      radial-gradient(circle at 100% 100%, rgba(201,160,58,.10), transparent 45%); }
  .cover-frame { position: absolute; inset: 0; }
  .club-mark { position: absolute; top: 240px; width: 100%; display: flex; justify-content: center; align-items: center; gap: 8px; }
  .club-mark-square { width: 12px; height: 12px; background: var(--line-green); }
  .club-mark-name { font-family: "Playfair Display", serif; font-weight: 500; font-size: 18px; color: var(--ink); }
  .cover-title { position: absolute; top: 296px; width: 100%; text-align: center; font-family: "Playfair Display", serif; font-weight: 500; font-size: 50px; color: var(--ink); letter-spacing: .005em; }
  .cover-subtitle { position: absolute; top: 380px; width: 100%; text-align: center; font-size: 10px; letter-spacing: .05em; color: var(--ink); text-transform: uppercase; }
  .cover-plus { position: absolute; top: 396px; width: 100%; text-align: center; font-size: 10px; color: var(--ink); }
  .cover-ball { position: absolute; left: 192px; top: 449px; width: 48px; height: 48px; border-radius: 50%; background: radial-gradient(circle at 35% 35%, #d3e85a, var(--ball)); }
</style>
</head>
<body>
  <div class="menu-folder">
    <section class="back-panel">
      <p class="back-intro">Tennis, Genuss und Freunde<br>Restaurant und Biergarten am Platz<br>mit Herz und Sonne</p>
      <div class="net-area" role="img" aria-label="Tennisnetz in hellem Beige"></div>
      <svg class="net-band" viewBox="0 0 296 40" preserveAspectRatio="none" aria-hidden="true">
        <path d="M0 22 Q148 -4 296 16" fill="none" stroke="var(--gold)" stroke-width="3"/>
      </svg>
      <div class="court-section">
        <svg class="court-lines" viewBox="0 0 296 355" aria-hidden="true">
          <line x1="0" y1="172" x2="296" y2="172" stroke="#f3f6ee" stroke-width="1.5"/>
          <line x1="148" y1="146" x2="148" y2="172" stroke="#f3f6ee" stroke-width="1.5"/>
          <line x1="0" y1="288" x2="296" y2="288" stroke="#f3f6ee" stroke-width="1.5"/>
        </svg>
        <div class="terrace-photo" role="img" aria-label="Foto: Terrasse mit Tischen und Stühlen vor dem Sandplatz"></div>
        <p class="season-note">Biergarten<br>Sommer<br>Saison</p>
        <p class="season-from">AB</p>
        <p class="back-footer">SPEISEKARTE &nbsp; Gartenweg 12 · 12345 Musterstadt · Tel 0123 456</p>
      </div>
    </section>

    <section class="cover-panel">
      <div class="cover-ornament" role="img" aria-label="Dekor: zarte Platzlinien-Bögen in Grün und Gold"></div>
      <svg class="cover-frame" viewBox="0 0 433 705" aria-hidden="true">
        <g fill="none">
          <path d="M36 18 H397 A14 14 0 0 0 411 32 V673 A14 14 0 0 0 397 687 H36 A14 14 0 0 0 22 673 V32 A14 14 0 0 0 36 18 Z" stroke="var(--ink)" stroke-width="1.5"/>
          <rect x="29" y="25" width="375" height="655" stroke="var(--line-green)" stroke-width="2"/>
        </g>
      </svg>
      <div class="club-mark">
        <span class="club-mark-square"></span>
        <span class="club-mark-name">Clubhaus Grünau</span>
      </div>
      <h1 class="cover-title">Speisekarte</h1>
      <p class="cover-subtitle">Tennis und Freizeit Restaurant</p>
      <p class="cover-plus">+</p>
      <div class="cover-ball" role="img" aria-label="Tennisball"></div>
    </section>
  </div>
</body>
</html>
```